I am a pastry chef and just started my own business. I make all sorts of pastries: french macarons, petit fours, artisan chocolates, artisan bread, and they can be ordered on the website. I'm obsessed with Wonderland, so I'd like to have a logo & a background that incorporate that, something whimsical. I was thinking of a white rabbit wearing a chef toque - maybe he could have a monocle on. The logo could go on one side of the business card with "Sugar Fox Patisserie Co" on a banner of some sort at the bottom, and the contact & info could go on the other side. I'd like a really light color as the background, maybe a really light yellow.

Industry/Entity Type

Chef

Contact Information for Business Card

Sugar Fox Patisserie Co
Mira Delcour Penhale
sugarfoxpatisserieco.shopvaleo.example
sugarfoxpatisserieco@mailvaleo.example
514-83-2071

```html
<!DOCTYPE html>
<html lang="en">
<head>
<meta charset="utf-8">
<title>Sugar Fox Patisserie Co — Business Card</title>
<link href="https://fonts.googleapis.com/css2?family=Caprasimo&family=Questrial&family=Sniglet:wght@800&display=swap" rel="stylesheet">
<style>
  :root {
    --page: #ffffff;
    --card: #ffffff;
    --lemon: #f0fc64;
    --ink: #111111;
    --shade: rgba(0,0,0,0.18);
  }
  html, body {
    margin: 0;
    padding: 0;
    width: 849px;
    height: 1200px;
    overflow: hidden;
    background: var(--page);
  }
  .canvas {
    position: relative;
    width: 849px;
    height: 1200px;
  }
  .card {
    position: absolute;
    left: 81px;
    width: 687px;
    height: 403px;
    border-radius: 28px;
    overflow: hidden;
    background: var(--card);
    box-shadow: 0 4px 18px var(--shade);
  }
  .card--back { top: 145px; }
  .card--front { top: 651px; }
  .card__waves {
    position: absolute;
    inset: 0;
    width: 687px;
    height: 403px;
  }
  .band { fill: var(--lemon); }
  .band-stripe { fill: none; stroke: #ffffff; stroke-width: 4; }
  .band-shadow { fill: none; stroke: rgba(0,0,0,0.22); stroke-width: 3; filter: blur(2px); }

  .holder-name {
    position: absolute;
    left: 54px;
    top: 138px;
    margin: 0;
    font-family: "Caprasimo", Georgia, serif;
    font-size: 29px;
    font-weight: 400;
    color: var(--ink);
    letter-spacing: 0.3px;
  }
  .contact-list {
    position: absolute;
    left: 278px;
    top: 213px;
    margin: 0;
    padding: 0;
    list-style: none;
    font-family: "Questrial", "Century Gothic", sans-serif;
    font-size: 19.5px;
    color: var(--ink);
  }
  .contact-list li {
    display: flex;
    align-items: center;
    height: 28px;
  }
  .contact-icon {
    width: 18px;
    height: 18px;
    margin-right: 12px;
    flex: none;
  }
  .contact-icon circle { fill: var(--lemon); }

  .brand-title {
    position: absolute;
    left: 0;
    right: 0;
    top: 130px;
    margin: 0;
    text-align: center;
    font-family: "Sniglet", "Arial Rounded MT Bold", sans-serif;
    font-weight: 800;
    font-size: 60px;
    line-height: 63px;
    letter-spacing: 3px;
    color: var(--ink);
    text-transform: uppercase;
  }
  .brand-url {
    position: absolute;
    left: 0;
    right: 0;
    top: 351px;
    margin: 0;
    text-align: center;
    font-family: "Questrial", "Century Gothic", sans-serif;
    font-size: 20px;
    letter-spacing: 1.2px;
    color: var(--ink);
  }
</style>
</head>
<body>
<main class="canvas">

  <section class="card card--back" aria-label="Contact side">
    <svg class="card__waves" viewBox="0 0 687 403" aria-hidden="true">
      <path class="band" d="M0 0H687V82C540 84 420 66 280 66C160 66 60 72 0 68Z"/>
      <path class="band-shadow" d="M0 72C60 76 160 70 280 70C420 70 540 88 687 86"/>
      <path class="band-stripe" d="M0 61C60 65 160 59 280 59C420 59 540 77 687 75"/>
      <path class="band-shadow" d="M0 322C100 316 220 314 340 318C470 322 580 330 687 326"/>
      <path class="band" d="M0 334C100 328 220 326 340 330C470 334 580 342 687 338V403H0Z"/>
      <path class="band-stripe" d="M0 330C100 324 220 322 340 326C470 330 580 338 687 334"/>
    </svg>

    <h1 class="holder-name">Mira Delcour Penhale</h1>

    <ul class="contact-list">
      <li>
        <svg class="contact-icon" viewBox="0 0 18 18" aria-hidden="true">
          <circle cx="9" cy="9" r="9"/>
          <path d="M6 4.5l2 2-1 1.2c.6 1.3 1.6 2.3 2.8 2.8l1.2-1 2 2-1.2 1.5C8.6 12.6 5.4 9.4 4.5 6.2Z" fill="#111"/>
        </svg>
        <span>514-83-2071</span>
      </li>
      <li>
        <svg class="contact-icon" viewBox="0 0 18 18" aria-hidden="true">
          <circle cx="9" cy="9" r="9"/>
          <rect x="4.5" y="6" width="9" height="6" fill="#111"/>
          <path d="M4.5 6L9 9.5 13.5 6" fill="none" stroke="#f0fc64" stroke-width="0.9"/>
        </svg>
        <span>sugarfoxpatisserieco@mailvaleo.example</span>
      </li>
      <li>
        <svg class="contact-icon" viewBox="0 0 18 18" aria-hidden="true">
          <circle cx="9" cy="9" r="9"/>
          <g fill="none" stroke="#111" stroke-width="1">
            <circle cx="9" cy="9" r="4.5"/>
            <ellipse cx="9" cy="9" rx="2" ry="4.5"/>
            <path d="M4.5 9h9M5.2 6.8h7.6M5.2 11.2h7.6"/>
          </g>
        </svg>
        <span>sugarfoxpatisserieco.shopvaleo.example</span>
      </li>
    </ul>
  </section>

  <section class="card card--front" aria-label="Brand side">
    <svg class="card__waves" viewBox="0 0 687 403" aria-hidden="true">
      <path class="band" d="M0 0H687V82C540 84 420 66 280 66C160 66 60 72 0 68Z"/>
      <path class="band-shadow" d="M0 72C60 76 160 70 280 70C420 70 540 88 687 86"/>
      <path class="band-stripe" d="M0 61C60 65 160 59 280 59C420 59 540 77 687 75"/>
      <path class="band-shadow" d="M0 322C100 316 220 314 340 318C470 322 580 330 687 326"/>
      <path class="band" d="M0 334C100 328 220 326 340 330C470 334 580 342 687 338V403H0Z"/>
      <path class="band-stripe" d="M0 330C100 324 220 322 340 326C470 330 580 338 687 334"/>
    </svg>

    <h2 class="brand-title">Sugar Fox<br>Patisserie Co</h2>
    <p class="brand-url">sugarfoxpatisserieco.shopvaleo.example</p>
  </section>

</main>
</body>
</html>
```